QUENBY DENTAL BLOG - Tooth Whitening Edition

Blog Design for Quenby Dental Practice. Quenby Dental is a dental practice that places emphasis on patient care. We provide high quality care and offer a wide variety of treatments.
Dental Implants, Crowns and Veneers and R tide Orthodontics are some of our Services
First Blog should Introduce us and our Services. We intend to link our blog to website- our website is to be redone but at the moment it is www.quenbydental-example.com.au
we should avoid putting pricing or promotions on the blog. focus on patient education and cosmetics
First Blog topic should centre on info and pt education around tooth whitening
some before and after photos of our patients are attached
link us on Chatterly
we are rated 5 stars on Finbo review and plum listings and it will be good if blog reflects this

Target Market(s)

Patients interested in Cosmetic/Aesthetic Dentistry

Industry/Entity Type

Dental

Font styles to use
Sans Serif
Decorative
Script

Requirements
Must have
• Quenby Dental Logo.
• Quenby Dental address and details
• Info and write up on tooth whitening
Nice to have
• Creative and attractive Blog that can be added to and built up overtime, i.e I can write future blog to this site
• link to website quenbydental-example.com.au
• showcase our high review ratings
• social media boost
• will be good if we can redraw/reanimate/design the pictures i have included in the blog write up- because they were copied from Finbo images- no copywrite
Should not have
• pricing or promotions

```html
<!DOCTYPE html>
<html lang="en">
<head>
<meta charset="utf-8">
<title>Quenby Dental Blog</title>
<link href="https://fonts.googleapis.com/css2?family=Oswald:wght@400;500&family=Roboto:wght@300;400;500&display=swap" rel="stylesheet">
<style>
:root{
  --blue:#2e74b5;
  --text:#333;
  --muted:#777;
  --grey-bg:#ececec;
  --white:#fff;
  --footer-dark:#222;
  --orange:#e06a1a;
  --star:#f4c21b;
  --like:#4267b2;
}
*{box-sizing:border-box;margin:0;padding:0}
html,body{width:684px;height:1200px;overflow:hidden}
body{position:relative;font-family:'Roboto',Arial,sans-serif;color:var(--text);background:var(--white)}
.abs{position:absolute}
.nowrap{white-space:nowrap}

/* header */
.site-header{left:0;top:0;width:684px;height:68px;background:var(--white)}
.brand{left:44px;top:8px;width:92px;height:90px;text-align:center}
.brand-mark{width:28px;height:28px;margin:0 auto;background:var(--blue);border-radius:50%}
.brand-name{margin-top:38px;font-family:'Oswald',sans-serif;font-size:11.5px;line-height:13px;color:var(--blue)}
.brand-tag{font-family:'Oswald',sans-serif;font-size:8px;line-height:11px;color:var(--blue)}
.main-nav{top:33px;left:0;width:684px;height:12px;font-size:8.5px;text-transform:uppercase}
.main-nav a{position:absolute;color:#222;text-decoration:none;white-space:nowrap}
.main-nav a.active{color:var(--blue)}
.login{left:588px;top:29px;width:44px;height:17px;background:var(--blue);color:#fff;font-size:7.5px;text-align:center;line-height:17px;border-radius:2px}

/* hero */
.hero{left:0;top:68px;width:684px;height:342px;background:linear-gradient(110deg,#dfe6ee 0%,#c9d3df 35%,#e9edf2 60%,#d8dfe8 100%)}
.hero-caption{left:49px;top:122px;width:348px;height:84px;background:rgba(70,120,175,.75)}
.hero-caption h1{position:absolute;left:18px;top:17px;font-family:'Oswald',sans-serif;font-weight:400;font-size:20px;line-height:26px;color:#fff;white-space:nowrap}
.hero-caption p{position:absolute;left:18px;top:48px;font-family:'Oswald',sans-serif;font-size:13.5px;line-height:18px;color:#fff;white-space:nowrap}
.hero-arrows{left:52px;top:220px;display:flex;gap:2px}
.hero-arrows span{width:17px;height:21px;background:#444;display:flex;align-items:center;justify-content:center}

/* content */
.content{left:0;top:410px;width:684px;height:615px;background:var(--grey-bg)}
.section-label{font-size:11.5px;line-height:14px;color:var(--blue);text-transform:uppercase;white-space:nowrap}
.pager{display:flex;gap:8px}
.card{background:var(--white);box-shadow:0 1px 4px rgba(0,0,0,.2)}
.photo{background:linear-gradient(135deg,#b78866,#7a4d38)}
.like{display:inline-block;background:var(--like);color:#fff;font-weight:500;text-align:center}

.feature{left:44px;top:472px;width:589px;height:150px}
.feature-img{left:11px;top:11px;width:140px;height:125px;background:linear-gradient(135deg,#4b5f78,#2b3a4e 60%,#6b7d92)}
.feature h2{left:173px;top:17px;font-weight:400;font-size:14.5px;line-height:18px;color:var(--blue);white-space:nowrap}
.feature h3{left:175px;top:41px;font-weight:400;font-size:9.8px;line-height:13px;color:#666;white-space:nowrap}
.feature p{left:175px;top:61px;width:392px;font-size:7.5px;line-height:17px;color:var(--muted)}
.feature .readmore{left:177px;top:122px;font-size:7.8px;line-height:10px;color:var(--orange);text-decoration:underline}
.feature .rating{left:444px;top:116px}
.feature .like{left:531px;top:116px;width:35px;height:13px;font-size:7.5px;line-height:13px}

.post{left:50px;width:401px;height:102px}
.post .photo{left:9px;top:8px;width:93px;height:83px}
.post h4{left:116px;top:13px;font-weight:400;font-size:10px;line-height:13px;color:var(--blue);white-space:nowrap}
.post .lead{left:116px;top:28px;font-size:6.4px;line-height:9px;color:#333;white-space:nowrap}
.post .body{left:116px;top:41px;width:272px;font-size:5.4px;line-height:11.5px;color:var(--muted)}
.post .body b{color:var(--orange);font-weight:400}
.post .meta{left:116px;top:80px;display:flex;gap:9px;align-items:center}
.post .like{width:22px;height:9px;font-size:5.5px;line-height:9px}

.latest{left:468px;top:662px;width:166px;height:323px}
.mini{position:absolute;left:0;width:166px;height:64px;border-bottom:1px solid #eee}
.mini .photo{position:absolute;left:12px;top:14px;width:30px;height:26px}
.mini p{position:absolute;left:49px;top:13px;width:108px;font-size:5.4px;line-height:9px;color:var(--muted)}
.mini span{position:absolute;left:51px;top:46px;font-size:5px;line-height:7px;font-style:italic;color:#555;white-space:nowrap}

/* footer */
.site-footer{left:0;top:1025px;width:684px;height:111px;background:var(--white)}
.fcol{top:22px}
.fcol h5{font-weight:400;font-size:9.5px;line-height:12px;color:var(--blue);margin-bottom:10px;text-transform:uppercase}
.fcol li{list-style:none;font-size:8px;color:#333;line-height:16.3px;white-space:nowrap}
.legal{left:0;top:1136px;width:684px;height:64px;background:var(--footer-dark);color:#fff}
.legal-links{left:51px;top:19px;font-size:8px;line-height:10px;white-space:nowrap}
.copyright{left:51px;top:35px;font-size:6.8px;line-height:9px;white-space:nowrap}
.social{left:541px;top:21px;display:flex;gap:6px}
.social span{width:18px;height:18px;border-radius:2px}
</style>
</head>
<body>

<svg width="0" height="0" style="position:absolute">
  <defs><path id="star" d="M7 1l1.8 4 4.2.4-3.2 2.8 1 4.2L7 10.2 3.2 12.4l1-4.2L1 5.4 5.2 5z"/></defs>
</svg>

<header class="site-header abs">
  <nav class="main-nav abs">
    <a class="active" href="#" style="left:195px">Home</a>
    <a href="#" style="left:244px">About Us</a>
    <a href="#" style="left:310px">Our Practice</a>
    <a href="#" style="left:397px">Online Shop</a>
    <a href="#" style="left:476px">FAQs</a>
    <a href="#" style="left:523px">Locate Us</a>
  </nav>
  <div class="login abs">LOG IN</div>
</header>

<section class="hero abs" role="img" aria-label="Hero photograph: a white tooth model beside a dental mirror on a bright blue-white surface">
  <div class="hero-caption abs">
    <h1>GENERAL AND PREVENTATIVE DENTISTRY</h1>
    <p>Lorem Ipsum has been the industry's standard dummy text</p>
  </div>
  <div class="hero-arrows abs">
    <span><svg width="7" height="12"><path d="M6 1L1 6l5 5" stroke="#fff" fill="none"/></svg></span>
    <span><svg width="7" height="12"><path d="M1 1l5 5-5 5" stroke="#fff" fill="none"/></svg></span>
  </div>
</section>

<div class="brand abs">
  <div class="brand-mark"></div>
  <div class="brand-name nowrap">QUENBY DENTAL</div>
  <div class="brand-tag nowrap">Putting patients first</div>
</div>

<main class="content abs"></main>

<div class="section-label abs" style="left:48px;top:453px">Blog :</div>
<div class="pager abs" style="left:608px;top:454px">
  <svg width="7" height="10"><path d="M5 1L1 5l4 4" stroke="#aaa" stroke-width="2" fill="none"/></svg>
  <svg width="7" height="10"><path d="M2 1l4 4-4 4" stroke="#aaa" stroke-width="2" fill="none"/></svg>
</div>

<article class="feature card abs">
  <div class="feature-img abs" role="img" aria-label="Diagram of hydroxyl radicals breaking down stain molecules into colourless molecules"></div>
  <h2 class="abs">Tooth Whitening</h2>
  <h3 class="abs">What Methods are there to Whiten teeth?</h3>
  <p class="abs">Tooth bleaching can be carried out using varying concentrations of Carbamide peroxide/ Hydrogen Peroxide Solution with a bleaching tray with varying treatment times. The treatment times range from 30minutes to over-night, depending on the type and concentration of solution used.</p>
  <a class="readmore abs" href="#">Read More</a>
  <svg class="rating abs" width="72" height="14" viewBox="0 0 74 14"><g fill="var(--star)" stroke="#b98a00" stroke-width=".5"><use href="#star"/><use href="#star" x="15"/><use href="#star" x="30"/><use href="#star" x="45"/><use href="#star" x="60"/></g></svg>
  <span class="like abs">Like</span>
</article>

<div class="section-label abs" style="left:51px;top:639px">Latest Blog:</div>
<div class="pager abs" style="left:436px;top:641px">
  <svg width="6" height="8"><path d="M4 1L1 4l3 3" stroke="#aaa" fill="none"/></svg>
  <svg width="6" height="8"><path d="M2 1l3 3-3 3" stroke="#aaa" fill="none"/></svg>
</div>
<div class="section-label abs" style="left:467px;top:637px">Latest Posts</div>

<article class="post card abs" style="top:662px">
  <div class="photo abs" role="img" aria-label="Patient photo showing a whitened smile"></div>
  <h4 class="abs">Mechanism of tooth Whitening</h4>
  <div class="lead abs">Hydrogen peroxide and Carbamide peroxide are the active ingredients in tooth whitening.</div>
  <div class="body abs">Lorem Ipsum has been the industry's standard dummy text ever since the 1500s, when an unknown printer took a galley of type and scrambled it to make a type specimen book. It has survived not centuries, but also the leap into electronic typesetting, remaining essentially unchanged..<b>MORE</b></div>
  <div class="meta abs"><svg width="48" height="9" viewBox="0 0 74 14"><g fill="var(--star)" stroke="#b98a00" stroke-width=".5"><use href="#star"/><use href="#star" x="15"/><use href="#star" x="30"/><use href="#star" x="45"/><use href="#star" x="60"/></g></svg><span class="like">Like</span></div>
</article>

<article class="post card abs" style="top:773px">
  <div class="photo abs" style="background:linear-gradient(135deg,#c99a6a,#a0663c)" role="img" aria-label="Before photo of a patient's smile with a missing tooth"></div>
  <h4 class="abs">Mechanism of tooth Whitening</h4>
  <div class="lead abs">Hydrogen peroxide and Carbamide peroxide are the active ingredients in tooth whitening.</div>
  <div class="body abs">Lorem Ipsum has been the industry's standard dummy text ever since the 1500s, when an unknown printer took a galley of type and scrambled it to make a type specimen book. It has survived not centuries, but also the leap into electronic typesetting, remaining essentially unchanged..<b>MORE</b></div>
  <div class="meta abs"><svg width="48" height="9" viewBox="0 0 74 14"><g fill="var(--star)" stroke="#b98a00" stroke-width=".5"><use href="#star"/><use href="#star" x="15"/><use href="#star" x="30"/><use href="#star" x="45"/><use href="#star" x="60"/></g></svg><span class="like">Like</span></div>
</article>

<article class="post card abs" style="top:883px">
  <div class="photo abs" style="background:linear-gradient(135deg,#c89080,#8e5548)" role="img" aria-label="After photo of a patient's whitened smile close-up"></div>
  <h4 class="abs">Mechanism of tooth Whitening</h4>
  <div class="lead abs">Hydrogen peroxide and Carbamide peroxide are the active ingredients in tooth whitening.</div>
  <div class="body abs">Lorem Ipsum has been the industry's standard dummy text ever since the 1500s, when an unknown printer took a galley of type and scrambled it to make a type specimen book. It has survived not centuries, but also the leap into electronic typesetting, remaining essentially unchanged..<b>MORE</b></div>
  <div class="meta abs"><svg width="48" height="9" viewBox="0 0 74 14"><g fill="var(--star)" stroke="#b98a00" stroke-width=".5"><use href="#star"/><use href="#star" x="15"/><use href="#star" x="30"/><use href="#star" x="45"/><use href="#star" x="60"/></g></svg><span class="like">Like</span></div>
</article>

<aside class="latest card abs">
  <div class="mini" style="top:0"><div class="photo" role="img" aria-label="Patient portrait"></div><p>Lorem Ipsum has been the industry's standard dummy text ever since the 1500s, when an unknown printer</p><span>Read More &gt;&gt;</span></div>
  <div class="mini" style="top:64px"><div class="photo" role="img" aria-label="Patient portrait"></div><p>Lorem Ipsum has been the industry's standard dummy text ever since the 1500s, when an unknown printer</p><span>Read More &gt;&gt;</span></div>
  <div class="mini" style="top:128px"><div class="photo" role="img" aria-label="Patient portrait"></div><p>Lorem Ipsum has been the industry's standard dummy text ever since the 1500s, when an unknown printer</p><span>Read More &gt;&gt;</span></div>
  <div class="mini" style="top:192px"><div class="photo" role="img" aria-label="Patient portrait"></div><p>Lorem Ipsum has been the industry's standard dummy text ever since the 1500s, when an unknown printer</p><span>Read More &gt;&gt;</span></div>
  <div class="mini" style="top:256px;border:0"><div class="photo" role="img" aria-label="Patient portrait"></div><p>Lorem Ipsum has been the industry's standard dummy text ever since the 1500s, when an unknown printer</p><span>Read More &gt;&gt;</span></div>
</aside>

<footer class="site-footer abs">
  <div class="fcol abs" style="left:53px"><h5>Link</h5><ul><li>About us</li><li>Services</li><li>Presentation</li></ul></div>
  <div class="fcol abs" style="left:154px"><h5>Specialists</h5><ul><li>Positioning</li><li>Our Opportunity</li><li>Our Customer</li></ul></div>
  <div class="fcol abs" style="left:269px"><h5>Advice</h5><ul><li>FAQs</li><li>Support</li></ul></div>
  <div class="fcol abs" style="left:374px"><h5>Agencies</h5><ul><li>Sign Up</li><li>Forums</li><li>Promotions</li></ul></div>
  <div class="fcol abs" style="left:481px"><h5>Contact Us</h5><ul><li>27 Harlow Lane, Westbrook, QD4 2LN</li><li>Phone: +1 555 019 2244</li><li>E-mail: hello@quenbydental-example.com.au</li></ul></div>
</footer>

<div class="legal abs">
  <div class="legal-links abs">Privacy Policy &nbsp;|&nbsp; Terms of Use &nbsp;|&nbsp; About Us &nbsp;|&nbsp; Sitemap</div>
  <div class="copyright abs">Copyright © 2015 &nbsp;All Rights</div>
  <div class="social abs">
    <span style="background:#2aa3e0"></span><span style="background:#c4302b"></span><span style="background:#3b5998"></span><span style="background:#0e76a8"></span>
  </div>
</div>

</body>
</html>
```